Web page for analytics company

Now that I have a new logo, I need a webpage design that will use it to its potential. Am looking for a design that handles presentation and access to data well - like sites with blocks that provide direct access to content without going through a set of menus. More like an infographic. No left/right menu bar.

I want the logo (attached) against a black background, but not text - not a fan of trying to read white text on a dark screen.

The website - torvimbly.com - currently has four pages - home, who we are, by the numbers and a blog.

The site will be done in Squarespace.

My apologies for not responding promptly - big report due today.  I will be online tomorrow with answers and feedback. 

Thanks!

```html
<!DOCTYPE html>
<html lang="en">
<head>
<meta charset="utf-8">
<title>Torvimbly – Velmora Equity Metrics</title>
<link rel="stylesheet" href="https://fonts.googleapis.com/css2?family=Open+Sans:wght@400;600&family=Carlito:wght@400;700&family=Asap:wght@600&display=swap">
<style>
  :root {
    --ink: #000000;
    --paper: #ffffff;
    --nav-grey: #d6d6d6;
    --accent: #f29a1f;
    --field-border: #3a3a3a;
    --band: rgba(255, 255, 255, 0.72);
    --photo-light: #eef1f4;
    --photo-blue: #7f9bbd;
    --photo-warm: #c89a5a;
    --photo-skin: #b98462;
  }
  * { box-sizing: border-box; margin: 0; padding: 0; }
  html, body { width: 911px; height: 1200px; overflow: hidden; }
  body {
    position: relative;
    background: var(--paper);
    color: var(--ink);
    font-family: "Carlito", "Open Sans", sans-serif;
  }

  /* Header */
  .site-header {
    position: absolute; top: 0; left: 0;
    width: 911px; height: 93px;
    background: var(--ink);
  }
  .main-nav a {
    position: absolute;
    font-family: "Open Sans", sans-serif;
    font-size: 12px; letter-spacing: 0.2px;
    color: var(--nav-grey); text-decoration: none;
  }
  .nav-home { left: 139px; top: 44px; }
  .nav-numbers { left: 204px; top: 44px; }
  .nav-who { left: 637px; top: 39px; }
  .nav-blog { left: 737px; top: 39px; }
  .brand {
    position: absolute; left: 340px; top: 22px;
    display: flex; align-items: center; gap: 14px;
  }
  .brand-dot {
    width: 46px; height: 46px; border-radius: 50%;
    background: var(--accent);
  }
  .brand-name {
    font-family: "Open Sans", sans-serif; font-weight: 600;
    font-size: 34px; color: var(--paper); line-height: 1;
  }
  .social-links {
    position: absolute; left: 630px; top: 85px;
    display: flex; gap: 4px; z-index: 3;
  }
  .social-links span {
    width: 20px; height: 20px; border-radius: 50%;
    background: var(--paper); border: 1px solid #888;
  }

  /* Hero */
  .hero {
    position: absolute; top: 93px; left: 0;
    width: 911px; height: 643px; overflow: hidden;
  }
  .hero-photo {
    position: absolute; inset: 0;
    background:
      radial-gradient(ellipse 260px 320px at 150px 260px, var(--photo-skin), transparent 70%),
      radial-gradient(ellipse 220px 300px at 360px 320px, var(--photo-warm), transparent 72%),
      radial-gradient(ellipse 300px 380px at 780px 380px, var(--photo-blue), transparent 75%),
      linear-gradient(100deg, #3c4f6e 0%, #d9dde3 45%, var(--photo-light) 70%, #9fb2c9 100%);
  }
  .hero-band {
    position: absolute; left: 0; top: 368px;
    width: 911px; height: 275px;
    background: var(--band);
    text-align: center;
  }
  .hero-title {
    margin-top: 47px;
    font-size: 37px; font-weight: 400; letter-spacing: 0.5px; line-height: 1;
  }
  .hero-tagline { margin-top: 7px; font-size: 19px; line-height: 22px; }
  .hero-copy {
    width: 632px; margin: 38px auto 0;
    font-size: 13px; line-height: 16px;
  }
  .btn {
    display: inline-block;
    background: var(--ink); color: var(--paper);
    border: 2px solid #8a8a8a;
    font-family: "Open Sans", sans-serif; font-size: 12.5px;
    text-decoration: none;
  }
  .hero .btn { margin-top: 30px; width: 107px; height: 33px; padding-top: 7px; }

  /* Subscribe */
  .subscribe {
    position: absolute; top: 736px; left: 0;
    width: 911px; height: 270px; text-align: center;
  }
  .subscribe h2 {
    margin-top: 37px;
    font-family: "Asap", sans-serif; font-weight: 600; font-size: 27px;
  }
  .subscribe p { margin-top: 12px; font-size: 16px; line-height: 20px; }
  .subscribe-form { position: relative; height: 80px; margin-top: 19px; }
  .field {
    position: absolute; top: 0; height: 34px;
    border: 3px double var(--field-border);
    font-family: "Open Sans", sans-serif; font-size: 13px;
    padding: 6px 13px; text-align: left; background: var(--paper);
  }
  .field-name { left: 184px; width: 268px; }
  .field-email { left: 467px; width: 269px; }
  .subscribe .btn {
    position: absolute; left: 404px; top: 41px;
    width: 108px; height: 34px; padding-top: 7px;
  }

  /* Footer */
  .site-footer {
    position: absolute; top: 1006px; left: 0;
    width: 911px; height: 194px;
    background: var(--ink); color: var(--paper);
    font-family: "Open Sans", sans-serif;
  }
  .partner {
    position: absolute; left: 135px; top: 26px;
    display: flex; align-items: center; gap: 6px;
    font-size: 15px;
  }
  .partner-dot { width: 16px; height: 16px; border-radius: 50%; background: #d83a2a; }
  .tweet {
    position: absolute; left: 143px; top: 66px; width: 150px;
    font-size: 7.5px; line-height: 11.5px; color: #ddd;
  }
  .tweet a { color: #ddd; }
  .contact h3 {
    position: absolute; left: 383px; top: 27px;
    font-weight: 400; font-size: 14px;
  }
  .contact-row {
    position: absolute; left: 383px; width: 127px;
    display: flex; justify-content: space-between; align-items: center;
    font-size: 8px;
  }
  .contact-row svg { width: 14px; height: 14px; }
  .row-follow { top: 63px; }
  .row-phone { top: 83px; }
  .row-mail { top: 102px; }
  .footer-brand {
    position: absolute; left: 556px; top: 34px;
    display: flex; align-items: center; gap: 12px;
  }
  .footer-brand .brand-dot { width: 40px; height: 40px; }
  .footer-brand .brand-name { font-size: 28px; }
  .legal a {
    position: absolute; top: 161px;
    font-size: 9.5px; color: var(--paper); text-decoration: none;
  }
  .legal-privacy { left: 135px; }
  .legal-terms { left: 211px; }
  .copyright { position: absolute; left: 558px; top: 161px; font-size: 9.5px; }
</style>
</head>
<body>

<header class="site-header">
  <nav class="main-nav">
    <a class="nav-home" href="#">HOME</a>
    <a class="nav-numbers" href="#">BY THE NUMBERS</a>
    <a class="nav-who" href="#">WHO WE ARE</a>
    <a class="nav-blog" href="#">BLOG</a>
  </nav>
  <div class="brand">
    <span class="brand-dot"></span>
    <span class="brand-name">Torvimbly</span>
  </div>
  <div class="social-links" aria-label="Social links">
    <span></span><span></span><span></span><span></span><span></span><span></span>
  </div>
</header>

<section class="hero">
  <div class="hero-photo" role="img" aria-label="Photo of two smiling colleagues reviewing charts on computer monitors"></div>
  <div class="hero-band">
    <h1 class="hero-title">VELMORA EQUITY METRICS</h1>
    <p class="hero-tagline">Enhancing Performance Through A Gender Lens</p>
    <p class="hero-copy">That’s where Torvimbly - Velmora Equity Metrics - comes in.&nbsp; Using the data-driven tools of gender analysis, we can help you determine if gender equity is being achieved - in businesses and organizations, in the planning and implementation of programs and services, and in the development and enforcement of public policy.</p>
    <a class="btn" href="#">READ MORE</a>
  </div>
</section>

<section class="subscribe">
  <h2>Subscribe To Our Mailing List</h2>
  <p>To keep up to date please Subscribe to our mailing list<br>Its FREE and EASY</p>
  <div class="subscribe-form">
    <div class="field field-name">Enter Your Name</div>
    <div class="field field-email">Enter Your Email Address</div>
    <a class="btn" href="#">REGISTER</a>
  </div>
</section>

<footer class="site-footer">
  <div class="partner"><span class="partner-dot"></span>Meridale Women Forum</div>
  <p class="tweet">Need to stop using “choices” as an excuse for gender inequality. Parallax Research says even w/ same choices women do less well. <a href="#">#equalitymeansjobs</a><br><a href="#">about 6 days ago</a></p>

  <div class="contact">
    <h3>Contact us</h3>
    <div class="contact-row row-follow">Follow us On Chirpline
      <svg viewBox="0 0 14 14"><circle cx="7" cy="7" r="7" fill="#fff"/></svg>
    </div>
    <div class="contact-row row-phone">555-014-2287
      <svg viewBox="0 0 14 14"><circle cx="7" cy="7" r="7" fill="#fff"/><path d="M4.5 3.5l1.5 0 .7 2-1 .8a5 5 0 0 0 2.5 2.5l.8-1 2 .7v1.5c-3.5.5-7-3-6.5-6.5z" fill="#000"/></svg>
    </div>
    <div class="contact-row row-mail">j.halden@torvimbly.com
      <svg viewBox="0 0 14 14"><circle cx="7" cy="7" r="7" fill="#fff"/><rect x="3.5" y="4.5" width="7" height="5" fill="none" stroke="#000" stroke-width="1"/><path d="M3.5 4.5L7 7.3l3.5-2.8" fill="none" stroke="#000" stroke-width="1"/></svg>
    </div>
  </div>

  <div class="footer-brand">
    <span class="brand-dot"></span>
    <span class="brand-name">Torvimbly</span>
  </div>

  <div class="legal">
    <a class="legal-privacy" href="#">Privacy policy</a>
    <a class="legal-terms" href="#">Terms &amp; conditions</a>
  </div>
  <p class="copyright">Copyright © 2014 Torvimbly. All rights reserved.</p>
</footer>

</body>
</html>
```